Hearth & Keg Room requires web site design - Casual restaurant

Need website designed for re-branding of Restaurant based in Fort Morgan, Colorado. We offer a wide variety of American cuisine in a casual, rustic atmosphere. We're offering 16 craft beers on draft, as well as a full service bar, and modern, interesting menu selections in a friendly, fun and energetic environment, with an emphasis on superior customer service and high quality, locally sourced food. We are a family, and community service oriented establishment. The website design should convey a welcoming sense, "simplicity", yet sophisticated - without pretentiousness. The website should effectively convey our "home style" relaxed atmosphere, as well as our casual character.

Business Hours: Sunday - Thursday, 11am-10pm / Friday & Saturday, 11am-11am

The Dunlo Hearth & Keg Room
2736 Pennick Road
Cedar Bluff, Ridgeland 00417
B: (970) 555-0173

WEBSITE ADDRESS: thedunlokegroom.com

Target Market(s)

Young Adults
Families
Blue and White Collar Americans
Senior Citizens
Small town location, appeal to everyone

Industry/Entity Type

American Restaurant

Contact Information for Business Card

Marcus T Ellery
Food & Beverage Director
2736 Pennick Road
B: (970) 555-0173
M: (231) 555-0148
mtellery@dunlokegroom.com
www.thedunlokegroom.com
***Use logo in uploaded files
***Open to single OR double sided
*** I will have additional names and information to add to this, for other employees.

Coding

Coded - Design and coding required

Number of Pages Required

5+ page

Font styles to use
Serif
Sans Serif
Decorative
Other font styles liked:
• Calafornian FB,

Requirements
Must have
• Home/Welcome Page
• Menu Page/Online Ordering Ready
• About Us/Contact Us page
• Catering/Private Events/Banquets Advertising section
• Ability to link to Facebook/TripAdvisor/Yelp/Instagram etc.
• Logo uploaded, reference for colors as well.
Nice to have
• About craft beer page
• Our Story/Bio section
• Photo Gallery
• Employment/Apply section
Should not have
• We are NOT a "fine dining" restaurant... think casual...

```html
<!DOCTYPE html>
<html lang="en">
<head>
<meta charset="utf-8">
<title>The Dunlo Hearth &amp; Keg Room</title>
<link href="https://fonts.googleapis.com/css2?family=Sorts+Mill+Goudy&family=Crimson+Text:wght@400;600;700&display=swap" rel="stylesheet">
<style>
:root{
  --green:#7b9b3b;
  --brown:#8a4519;
  --blue:#1d9ad6;
  --charcoal:#3b3b3b;
  --footer:#20232c;
  --footer-line:#3a3e49;
  --ink:#2b2b2b;
  --muted:#666;
  --price:#c4432f;
  --white:#fff;
}
*{box-sizing:border-box;margin:0;padding:0}
html,body{width:1200px;height:3622px;overflow:hidden}
body{position:relative;background:var(--white);font-family:"Crimson Text",Georgia,serif;color:var(--ink)}
.abs{position:absolute}
.heading{font-family:"Sorts Mill Goudy",Georgia,serif;font-weight:400}
.btn{position:absolute;display:flex;align-items:center;justify-content:center;background:var(--green);color:var(--white);border-radius:24px;font-weight:600;font-size:16px}

/* header */
.site-header{left:0;top:0;width:1200px;height:104px;background:var(--white)}
.brand{left:80px;top:30px;display:flex;align-items:center;gap:10px;font-family:"Crimson Text",serif;font-weight:700;font-size:34px;color:var(--ink)}
.brand-mark{width:14px;height:14px;background:var(--ink)}
.nav{left:400px;top:38px;display:flex;gap:20px;font-size:16px;color:#333}
.nav-reserve{left:990px;top:36px;width:123px;height:32px;background:var(--brown);color:var(--white);font-size:15px;display:flex;align-items:center;justify-content:center}

/* hero */
.hero{left:0;top:104px;width:1200px;height:456px;background:linear-gradient(135deg,#4a3426 0%,#8a6a50 35%,#5a4a3e 65%,#2a241f 100%)}
.hero-title{left:0;top:240px;width:1200px;text-align:center;color:var(--white);font-size:44px}
.hero-text{left:240px;top:302px;width:720px;text-align:center;color:var(--white);font-size:16px;line-height:27px}
.hero-arrow{top:310px}
.notch{position:absolute;left:545px;width:110px;height:30px}

/* welcome */
.welcome-title{left:0;top:640px;width:1200px;text-align:center;font-size:31px}
.welcome-text{left:160px;top:712px;width:880px;text-align:center;font-size:14px;line-height:29px;color:var(--muted)}

/* menu */
.menu-band{left:0;top:1016px;width:1200px;height:633px;background:linear-gradient(180deg,#3a2a1e,#5a4030 50%,#2e2218)}
.menu-panel{left:89px;top:1098px;width:1024px;height:471px;background:var(--white)}
.menu-label{left:138px;top:1134px;font-size:32px}
.menu-title{left:138px;top:1178px;font-size:39px;line-height:46px;color:var(--brown)}
.menu-text{left:138px;top:1286px;width:330px;font-size:13.5px;line-height:23px;color:var(--muted)}
.menu-link{left:138px;top:1384px;font-size:14px;border-bottom:1px solid var(--ink);padding-bottom:2px}
.dish-card{background:var(--white);box-shadow:0 4px 18px rgba(0,0,0,.25);padding:14px 14px;overflow:hidden}
.dish{display:flex;gap:12px;padding:12px 0;border-bottom:1px solid #e2e2e2}
.dish:last-child{border-bottom:0}
.dish-photo{flex:0 0 62px;height:62px;border-radius:50%;background:radial-gradient(circle,#b57a45,#6e4326)}
.dish-name{font-size:13px;font-weight:700;letter-spacing:.3px;white-space:nowrap}
.dish-desc{font-size:11.5px;line-height:15px;color:#555}
.dish-price{font-size:11.5px;color:var(--price);margin-top:3px;white-space:nowrap}
.slider-btn{top:1526px;width:42px;height:43px;background:#6b6b6b;display:flex;align-items:center;justify-content:center}

/* gallery */
.gallery-title{left:0;top:1740px;width:1200px;text-align:center;font-size:31px}
.gallery-photo{top:1840px;height:280px}

/* reservation */
.reserve{left:0;top:2257px;width:1200px;height:514px;background:linear-gradient(120deg,#3a2a20,#6e5240 45%,#4a3a30 70%,#221c18)}
.reserve-kicker{left:0;top:2325px;width:1200px;text-align:center;color:var(--white);font-size:29px}
.reserve-title{left:0;top:2378px;width:1200px;text-align:center;color:var(--white);font-size:37px}
.field{position:absolute;height:67px;background:rgba(255,255,255,.35);color:var(--white);font-size:19px;display:flex;align-items:center;justify-content:space-between;padding:0 22px}

/* info boxes */
.info-box{top:2890px;height:321px;border-radius:22px;color:var(--white);text-align:center}
.info-title{font-size:31px;margin-top:44px}
.info-strong{font-size:21px;font-weight:700;margin-top:16px;line-height:32px}
.info-line{font-size:17px;line-height:31px}

/* footer */
.site-footer{left:0;top:3312px;width:1200px;height:310px;background:var(--footer);color:var(--white)}
.foot-brand{left:84px;top:3410px;display:flex;align-items:center;gap:10px;font-weight:700;font-size:40px}
.foot-heading{font-size:22px;top:3400px}
.foot-input{left:350px;top:3445px;width:331px;height:58px;border:1px solid #555a66;background:#2b2f39;color:#888;font-size:12px;display:flex;align-items:center;padding-left:18px}
.foot-sub{left:702px;top:3445px;width:169px;height:58px;background:var(--green);font-size:16px;display:flex;align-items:center;justify-content:center}
.social{top:3462px;width:26px;height:26px;background:var(--white);border-radius:3px}
.foot-rule{left:84px;top:3544px;width:1032px;height:1px;background:var(--footer-line)}
.foot-links{left:84px;top:3566px;font-size:12px;color:#ccc}
.foot-copy{right:84px;top:3566px;font-size:12px;color:#ccc}
</style>
</head>
<body>

<header class="site-header abs">
  <div class="brand abs"><span class="brand-mark"></span>Dunlo</div>
  <nav class="nav abs"><span>Home</span><span>Menu</span><span>Online Order</span><span>About us</span><span>Private Events</span><span>Banquets</span><span>Contact us</span></nav>
  <div class="nav-reserve abs">Reservation</div>
</header>

<section class="hero abs" role="img" aria-label="Friends laughing and toasting with wine glasses at a restaurant table"></section>
<h1 class="hero-title abs heading">The Dunlo Hearth &amp; Keg Room</h1>
<p class="hero-text abs">Lorem Ipsum is simply dummy text of the printing and typesetting industry. Lorem Ipsum has been the industry's standard dummy text ever since the 1500s</p>
<div class="btn" style="left:509px;top:386px;width:179px;height:56px">Read More</div>
<svg class="abs hero-arrow" style="left:28px" width="24" height="46" viewBox="0 0 24 46"><path d="M22 2 L3 23 L22 44" fill="none" stroke="#fff" stroke-width="3"/></svg>
<svg class="abs hero-arrow" style="left:1148px" width="24" height="46" viewBox="0 0 24 46"><path d="M2 2 L21 23 L2 44" fill="none" stroke="#fff" stroke-width="3"/></svg>
<svg class="notch" style="top:559px" viewBox="0 0 110 30"><path d="M0 0 Q40 0 48 20 L55 30 L62 20 Q70 0 110 0Z" fill="#3a2c24"/></svg>

<section>
  <h2 class="welcome-title abs heading">Welcome to The Dunlo Hearth &amp; Keg Room</h2>
  <p class="welcome-text abs">Lorem Ipsum is simply dummy text of the printing and typesetting industry. Lorem Ipsum has been the industry's standard dummy text ever since the 1500s, when an unknown printer took a galley of type and scrambled it to make a type specimen book. It has survived not only five centuries, but also the leap into electronic typesetting, remaining essentially unchanged. It was popularised in the 1960s with the release of Letraset sheets containing Lorem Ipsum passages, and more recently with desktop publishing software like Aldus PageMaker including versions of Lorem Ipsum.</p>
  <div class="btn" style="left:528px;top:834px;width:143px;height:46px;font-size:14px">Read More</div>
</section>

<section>
  <div class="menu-band abs" role="img" aria-label="Overhead view of fresh vegetables, grilled food and sauces on a dark wooden table"></div>
  <div class="menu-panel abs"></div>
  <div class="menu-label abs heading">Menu</div>
  <h2 class="menu-title abs heading">Something Special<br>From The Dunlo</h2>
  <p class="menu-text abs">Lorem Ipsum is simply dummy text of the printing and typesetting industry. Lorem Ipsum has been the industry's standard dummy text ever since the 1500s.</p>
  <div class="menu-link abs">View Special Menu</div>

  <div class="dish-card abs" style="left:512px;top:1183px;width:304px;height:319px">
    <div class="dish"><div class="dish-photo" role="img" aria-label="Salmon sandwich"></div><div><div class="dish-name">SALMON BLT</div><div class="dish-desc">Grilled salmon, crisp bacon, lettuce and tomato on toasted sourdough</div><div class="dish-price">$11.99</div></div></div>
    <div class="dish"><div class="dish-photo" role="img" aria-label="Fish and chips"></div><div><div class="dish-name">FISH &amp; CHIPS</div><div class="dish-desc">Beer battered cod, hand cut fries, slaw and house tartar</div><div class="dish-price">2pc ... $12.99 | 3pc ... $15.99</div></div></div>
    <div class="dish"><div class="dish-photo" role="img" aria-label="Battered shrimp"></div><div><div class="dish-name">BEER BATTERED SHRIMP</div><div class="dish-desc">Gulf shrimp in light beer batter with fries and cocktail sauce</div><div class="dish-price">6pc ... $14.99 | 9pc ... $17.99</div></div></div>
  </div>

  <div class="dish-card abs" style="left:700px;top:1127px;width:355px;height:363px">
    <div class="dish"><div class="dish-photo" role="img" aria-label="Country fried steak plate"></div><div><div class="dish-name">COUNTRY FRIED STEAK</div><div class="dish-desc">Hand cut sirloin, breaded in house, whipped potatoes and brown gravy</div><div class="dish-price">Half ... $12.99 | Full ... $15.99</div></div></div>
    <div class="dish"><div class="dish-photo" role="img" aria-label="Nacho platter"></div><div><div class="dish-name">NACHO GRANDE</div><div class="dish-desc">Shredded chicken, black beans, lettuce, fresh tomato, jalapeño and corn chips</div><div class="dish-price">Half ... $9.99 | Full ... $12.99</div></div></div>
    <div class="dish"><div class="dish-photo" role="img" aria-label="Braised pot roast"></div><div><div class="dish-name">BEER BRAISED POT ROAST</div><div class="dish-desc">Slow braised chuck roast with carrots, whipped potatoes and rich beer gravy</div><div class="dish-price">Half ... $13.99 | Full ... $16.99</div></div></div>
  </div>

  <div class="slider-btn abs" style="left:1028px"><svg width="12" height="18" viewBox="0 0 12 18"><path d="M10 2 L3 9 L10 16" fill="none" stroke="#fff" stroke-width="2.5"/></svg></div>
  <div class="slider-btn abs" style="left:1071px;background:#3e3e3e"><svg width="12" height="18" viewBox="0 0 12 18"><path d="M2 2 L9 9 L2 16" fill="none" stroke="#fff" stroke-width="2.5"/></svg></div>
  <svg class="notch" style="top:1648px" viewBox="0 0 110 30"><path d="M0 0 Q40 0 48 20 L55 30 L62 20 Q70 0 110 0Z" fill="#2e2218"/></svg>
</section>

<section>
  <h2 class="gallery-title abs heading">The Dunlo Hearth &amp; Keg Room Gallery</h2>
  <div class="gallery-photo abs" style="left:0;width:290px;background:linear-gradient(160deg,#3a2a22,#6a4a34)" role="img" aria-label="Busy dining room with guests at tables"></div>
  <div class="gallery-photo abs" style="left:302px;width:292px;background:linear-gradient(160deg,#4a2a18,#2a1a12)" role="img" aria-label="Wine bottles lined up in front of stacked firewood"></div>
  <div class="gallery-photo abs" style="left:604px;width:292px;background:linear-gradient(160deg,#2a2030,#6a3a3a)" role="img" aria-label="Glasses of red wine raised in a toast"></div>
  <div class="gallery-photo abs" style="left:906px;width:294px;background:linear-gradient(160deg,#3a2418,#7a5038)" role="img" aria-label="Friends toasting drinks at the bar"></div>
</section>

<section>
  <svg class="notch" style="top:2228px" viewBox="0 0 110 30"><path d="M0 30 Q40 30 48 10 L55 0 L62 10 Q70 30 110 30Z" fill="#3a2a20"/></svg>
  <div class="reserve abs" role="img" aria-label="Group of friends smiling and toasting at a dinner table"></div>
  <div class="reserve-kicker abs heading">Book a Table</div>
  <h2 class="reserve-title abs heading">Make a Reservation</h2>
  <div class="field" style="left:203px;top:2453px;width:248px">Select Date
    <svg width="20" height="20" viewBox="0 0 20 20"><rect x="2" y="4" width="16" height="14" fill="none" stroke="#fff" stroke-width="2"/><path d="M2 8 H18 M6 2 V6 M14 2 V6" stroke="#fff" stroke-width="2"/></svg></div>
  <div class="field" style="left:476px;top:2453px;width:248px">Select Time
    <svg width="20" height="20" viewBox="0 0 20 20"><circle cx="10" cy="10" r="8" fill="none" stroke="#fff" stroke-width="2"/><path d="M10 5 V10 L13 13" fill="none" stroke="#fff" stroke-width="2"/></svg></div>
  <div class="field" style="left:746px;top:2453px;width:249px">Party Size</div>
  <div class="field" style="left:203px;top:2540px;width:386px">Name</div>
  <div class="field" style="left:608px;top:2540px;width:387px">Email</div>
  <div class="btn" style="left:488px;top:2629px;width:222px;height:68px;border-radius:34px;font-size:19px;font-weight:400">Reserve Now</div>
  <svg class="notch" style="top:2770px" viewBox="0 0 110 30"><path d="M0 0 Q40 0 48 20 L55 30 L62 20 Q70 0 110 0Z" fill="#2a221c"/></svg>
</section>

<section>
  <svg class="notch" style="left:276px;top:2862px" viewBox="0 0 110 30"><path d="M0 30 Q40 30 48 10 L55 0 L62 10 Q70 30 110 30Z" fill="var(--blue)"/></svg>
  <div class="info-box abs" style="left:97px;width:468px;background:var(--blue)">
    <div class="info-title heading">Directions</div>
    <div class="info-strong">The Dunlo Hearth &amp; Keg Room</div>
    <div class="info-line"><svg width="12" height="15" viewBox="0 0 12 16"><path d="M6 0 C2.5 0 0 2.6 0 6 C0 10 6 16 6 16 C6 16 12 10 12 6 C12 2.6 9.5 0 6 0Z" fill="#fff"/><circle cx="6" cy="6" r="2.2" fill="var(--blue)"/></svg> 2736 Pennick Road, Cedar Bluff, Ridgeland 00417</div>
    <div class="info-line"><svg width="14" height="14" viewBox="0 0 16 16"><path d="M3 1 L6 1 L7 5 L5 6.5 C6 9 7 10 9.5 11 L11 9 L15 10 L15 13 C15 14 14 15 13 15 C6 15 1 10 1 3 C1 2 2 1 3 1Z" fill="#fff"/></svg> (555) 555-0173</div>
    <div class="info-line" style="margin-top:22px;text-decoration:underline">View map</div>
  </div>
  <svg class="notch" style="left:276px;top:3210px" viewBox="0 0 110 30"><path d="M0 0 Q40 0 48 20 L55 30 L62 20 Q70 0 110 0Z" fill="var(--blue)"/></svg>

  <svg class="notch" style="left:816px;top:2862px" viewBox="0 0 110 30"><path d="M0 30 Q40 30 48 10 L55 0 L62 10 Q70 30 110 30Z" fill="var(--charcoal)"/></svg>
  <div class="info-box abs" style="left:637px;width:469px;background:var(--charcoal)">
    <div class="info-title heading">Business Hours</div>
    <div class="info-strong">Sunday - Thursday, 11am-10pm<br>Friday &amp; Saturday, 11am-11am</div>
  </div>
  <svg class="notch" style="left:816px;top:3210px" viewBox="0 0 110 30"><path d="M0 0 Q40 0 48 20 L55 30 L62 20 Q70 0 110 0Z" fill="var(--charcoal)"/></svg>
</section>

<footer class="site-footer abs"></footer>
<div class="foot-brand abs" style="color:#fff"><span class="brand-mark" style="background:#fff"></span>Dunlo</div>
<div class="foot-heading abs" style="left:354px;color:#fff">Get news &amp; offers</div>
<div class="foot-input abs">Your Email</div>
<div class="foot-sub abs" style="color:#fff">Subscribe</div>
<div class="foot-heading abs" style="left:918px;color:#fff">Follow Us</div>
<div class="social abs" style="left:912px"></div>
<div class="social abs" style="left:957px"></div>
<div class="social abs" style="left:1003px"></div>
<div class="social abs" style="left:1049px"></div>
<div class="foot-rule abs"></div>
<div class="foot-links abs">Home &nbsp;|&nbsp; Menu &nbsp;|&nbsp; Online Order &nbsp;|&nbsp; About us &nbsp;|&nbsp; Private Events &nbsp;|&nbsp; Banquets &nbsp;|&nbsp; Contact us</div>
<div class="foot-copy abs">© 2017 The Dunlo Hearth &amp; Keg Room. All Rights Reserved.</div>

</body>
</html>
```